Company Postage Label

Design a postage label that measures: 16cm long x 9cm high with a sticky back to stick on boxes. Similar to the attached from Talvora Carriers.

Industry/Entity Type

Motorcycle Part

Colors

Designer to choose colors to be used in the design.

Requirements
Must have
• Company logo and address

```html
<!DOCTYPE html>
<html lang="en">
<head>
<meta charset="utf-8">
<title>Ridgeline Moto Parts – Postage Label</title>
<link rel="stylesheet" href="https://fonts.googleapis.com/css2?family=Arimo:wght@400;700&display=swap">
<style>
  :root {
    --page: #e9e7e3;
    --frame: #262626;
    --paper: #eef2f0;
    --ink: #1c1c1c;
    --muted: #3a3a3a;
    --brand: #b3201f;
  }
  html, body {
    margin: 0;
    width: 1200px;
    height: 800px;
    overflow: hidden;
    background: var(--page);
    font-family: "Arimo", Arial, sans-serif;
  }
  .canvas {
    position: relative;
    width: 1200px;
    height: 800px;
  }
  .label {
    position: absolute;
    left: 120px;
    top: 130px;
    width: 960px;
    height: 540px;
    box-sizing: border-box;
    background: var(--frame);
    padding: 20px;
  }
  .label-inner {
    position: relative;
    width: 100%;
    height: 100%;
    display: flex;
    gap: 14px;
  }
  .panel {
    background: var(--paper);
    position: relative;
    box-sizing: border-box;
  }
  .panel-sender {
    width: 300px;
    padding: 34px 30px 28px;
    display: flex;
    flex-direction: column;
  }
  .panel-recipient {
    flex: 1;
    padding: 30px 34px 28px 34px;
  }
  .write-line {
    border-bottom: 2px solid var(--ink);
    height: 54px;
  }
  .sender-lines .write-line { height: 50px; }
  .from-label {
    margin-top: auto;
    font-size: 22px;
    color: var(--ink);
  }
  .brand {
    display: flex;
    align-items: center;
    gap: 10px;
  }
  .brand-mark {
    width: 22px;
    height: 22px;
    border-radius: 50%;
    background: var(--brand);
  }
  .brand-name {
    font-size: 20px;
    font-weight: 700;
    color: var(--brand);
    letter-spacing: 0.5px;
  }
  .return-address {
    margin: 8px 0 0 32px;
    font-size: 13px;
    color: var(--muted);
  }
  .stamp-boxes {
    position: absolute;
    top: 30px;
    right: 34px;
    display: flex;
  }
  .stamp-box {
    width: 44px;
    height: 44px;
    border: 2px solid var(--ink);
    margin-left: -2px;
  }
  .recipient-lines {
    position: absolute;
    left: 110px;
    right: 34px;
    top: 90px;
  }
  .contact {
    position: absolute;
    left: 34px;
    bottom: 26px;
    font-size: 13px;
    color: var(--muted);
    line-height: 1.6;
  }
</style>
</head>
<body>
<main class="canvas">
  <section class="label" aria-label="Postage label">
    <div class="label-inner">
      <div class="panel panel-sender">
        <div class="sender-lines">
          <div class="write-line"></div>
          <div class="write-line"></div>
          <div class="write-line"></div>
          <div class="write-line"></div>
          <div class="write-line"></div>
          <div class="write-line"></div>
          <div class="write-line"></div>
        </div>
        <div class="from-label">From:</div>
      </div>
      <div class="panel panel-recipient">
        <div class="brand">
          <span class="brand-mark"></span>
          <span class="brand-name">Ridgeline Moto Parts</span>
        </div>
        <p class="return-address">18 Harlow Road, Ferndale, QLD 4210</p>
        <div class="stamp-boxes">
          <div class="stamp-box"></div>
          <div class="stamp-box"></div>
          <div class="stamp-box"></div>
        </div>
        <div class="recipient-lines">
          <div class="write-line"></div>
          <div class="write-line"></div>
          <div class="write-line"></div>
          <div class="write-line"></div>
          <div class="write-line"></div>
          <div class="write-line"></div>
        </div>
        <div class="contact">
          <div>E: orders@ridgelinemoto.net.au</div>
          <div>WWW.RIDGELINEMOTO.COM</div>
        </div>
      </div>
    </div>
  </section>
</main>
</body>
</html>
```